Marlow Estate Group (Real Estate and Investment)

A high end, clean design.
We are a real estate company with sales, asset management and investment divisions. We want to use a black and white scheme which is really high end feel. The back of the card can just be the logo (black background with the white writing) as we will probably emboss this when we print)

Target Market(s)

High level investors, high end houses for sale

Industry/Entity Type

Business

Contact Information for Business Card

Name, position, phone number and email address
Ben Marlow, Managing Director, 0438926057 and ben@marlowestate.com.au

Requirements
Must have
• Back of the card to be the black background with the white writing (as per the attached images). Would like the capacity to emboss the writing and logo

```html
<!DOCTYPE html>
<html lang="en">
<head>
<meta charset="utf-8">
<title>Marlow Estate Group – Business Card</title>
<link href="https://fonts.googleapis.com/css2?family=Lato:wght@300;400;700&family=Raleway:wght@400&display=swap" rel="stylesheet">
<style>
  :root {
    --backdrop: #2a2a2a;
    --card: #000000;
    --ink: #ffffff;
    --ink-soft: #e6e6e6;
  }
  * { margin: 0; padding: 0; box-sizing: border-box; }
  html, body {
    width: 1200px;
    height: 680px;
    overflow: hidden;
    background: var(--backdrop);
  }
  .stage {
    width: 1200px;
    height: 680px;
    display: flex;
    align-items: center;
    justify-content: center;
    gap: 40px;
  }
  .card {
    width: 520px;
    height: 318px;
    background: var(--card);
    color: var(--ink);
    position: relative;
    box-shadow: 0 10px 30px rgba(0,0,0,0.45);
  }
  /* back of card */
  .card-back {
    display: flex;
    flex-direction: column;
    align-items: center;
    justify-content: center;
    gap: 26px;
  }
  .brand-mark {
    width: 96px;
    height: 96px;
    border: 1.5px solid var(--ink);
    border-radius: 50%;
  }
  .brand-name {
    font-family: "Raleway", sans-serif;
    font-weight: 400;
    font-size: 26px;
    letter-spacing: 0.06em;
    text-transform: uppercase;
    color: var(--ink);
  }
  /* front of card */
  .card-front {
    display: flex;
    align-items: center;
  }
  .holder {
    position: absolute;
    left: 0;
    width: 250px;
    top: 176px;
    text-align: right;
    padding-right: 34px;
  }
  .holder-name {
    font-family: "Lato", sans-serif;
    font-weight: 700;
    font-size: 24px;
    letter-spacing: 0.01em;
    line-height: 1.1;
  }
  .holder-role {
    font-family: "Lato", sans-serif;
    font-weight: 400;
    font-size: 14px;
    color: var(--ink-soft);
    letter-spacing: 0.03em;
    margin-top: 2px;
  }
  .divider {
    position: absolute;
    left: 262px;
    top: 128px;
    width: 1px;
    height: 86px;
    background: var(--ink);
  }
  .contact {
    position: absolute;
    left: 292px;
    top: 140px;
    list-style: none;
    font-family: "Lato", sans-serif;
    font-weight: 400;
    font-size: 13px;
    color: var(--ink);
  }
  .contact li {
    display: flex;
    align-items: center;
    gap: 10px;
    height: 22px;
  }
  .contact svg { width: 12px; height: 12px; flex: none; }
</style>
</head>
<body>
  <main class="stage">
    <section class="card card-back" aria-label="Card back">
      <div class="brand-mark"></div>
      <p class="brand-name">Marlow Estate Group</p>
    </section>

    <section class="card card-front" aria-label="Card front">
      <div class="holder">
        <p class="holder-name">Ben Marlow</p>
        <p class="holder-role">Managing Director</p>
      </div>
      <div class="divider"></div>
      <ul class="contact">
        <li>
          <svg viewBox="0 0 24 24" aria-hidden="true"><path fill="#fff" d="M6.6 10.8a15.1 15.1 0 0 0 6.6 6.6l2.2-2.2c.3-.3.7-.4 1-.2 1.1.4 2.3.6 3.6.6.6 0 1 .4 1 1V20c0 .6-.4 1-1 1A17 17 0 0 1 3 4c0-.6.4-1 1-1h3.5c.6 0 1 .4 1 1 0 1.3.2 2.5.6 3.6.1.3 0 .7-.2 1z"/></svg>
          <span>043 892 6057</span>
        </li>
        <li>
          <svg viewBox="0 0 24 24" aria-hidden="true"><rect x="2" y="5" width="20" height="14" fill="#fff"/><path d="M2 5l10 8 10-8" fill="none" stroke="#000" stroke-width="1.6"/></svg>
          <span>ben@marlowestate.com.au</span>
        </li>
      </ul>
    </section>
  </main>
</body>
</html>
```